Banner Ad Design Project: rovalenmotors.com

Google all ad dimensions banner pack for http://www.rovalenmotors.com.

Ad dimensions Max. file sizes (KB) Ad types
468 × 60 50 Banner
728 × 90 50 Leaderboard
250 × 250 50 Square
200 × 200 50 Small square
336 × 280 50 Large rectangle
300 × 250 50 Inline rectangle
120 × 600 50 Skyscraper
160 × 600 50 Wide skyscraper
300 × 600 200 Half-page ad
970 × 90 200 Large leaderboard
240 × 400 50 Vertical rectangle
980 × 120 200 Panorama
930 × 180 200 Top banner
250 × 360 50 Triple widescreen
580 × 400 200 Netboard

*Please visit the website and come up with unique ideas.

Target Market(s)

Consumers looking to transport a car, motor vehicle, motorcycle or anything that has wheels and a motor in the united states long distance.

Industry/Entity Type

Google

Requirements
Must have
• a call to action for example (RANDOM ONE):
-
TALK TO A REAL CAR SHIPPING PRO NOW: 1-888-514-2763
HAVE CAR TRANSPORT QUESTIONS? CALL NOW: 1-888-514-2763
CALL NOW & TALK TO A REAL AUTO SHIPPING EXPERT: 1-888-514-2763
Call Now Free Quote:1-888-514-2763

Nice to have
• Best Value For Dollar Auto Transport
Bonded, Insured & Licensed
Price Match Guarantee: will match any price by a 4 or 5 star rated Company.
Best of all, you pay nothing until your car is picked up!
Nationwide Door-To-Door Vehicle Shipping
Should not have
• Logo integrated in to the design.
bold call to action; ex; call now free quote:
Heading style phone number, 888-514-2763, stands out and screams call now.
example:
CALL ROVALEN TODAY TO TRANSPORT YOUR VEHICLE
1-888-514-2763

```html
<!DOCTYPE html>
<html lang="en">
<head>
<meta charset="utf-8">
<title>Rovalen Banner Pack</title>
<link href="https://fonts.googleapis.com/css2?family=Roboto+Condensed:wght@400;700&display=swap" rel="stylesheet">
<style>
  :root {
    --page: #ecebe8;
    --navy-dark: #1b2436;
    --navy-mid: #2c3e5a;
    --navy-light: #4a6a92;
    --band-start: #2a6ea8;
    --band-end: #8ec3e6;
    --phone: #e4f21c;
    --white: #ffffff;
    --brand-blue: #2b6da6;
    --photo-hair: #d9b06a;
    --photo-shirt: #e8eef4;
  }
  * { box-sizing: border-box; margin: 0; padding: 0; }
  html, body { width: 1200px; height: 800px; overflow: hidden; }
  body {
    position: relative;
    background: var(--page);
    font-family: "Roboto Condensed", "Arial Narrow", sans-serif;
    color: var(--white);
  }
  .ad { position: absolute; overflow: hidden; background: var(--white); box-shadow: 0 2px 8px rgba(0,0,0,.18); }
  .panel-dark { position: absolute; background: linear-gradient(180deg, var(--navy-dark) 0%, var(--navy-mid) 55%, var(--navy-light) 100%); }
  .band { position: absolute; background: linear-gradient(90deg, var(--band-start), var(--band-end)); }
  .photo {
    position: absolute;
    background: radial-gradient(ellipse at 50% 35%, var(--photo-hair) 0%, #c79a58 28%, var(--photo-shirt) 62%, #c9d3de 100%);
  }
  .notch-up { position: absolute; width: 0; height: 0; border-left: 9px solid transparent; border-right: 9px solid transparent; border-bottom: 10px solid var(--white); }
  .notch-right { position: absolute; width: 0; height: 0; border-top: 9px solid transparent; border-bottom: 9px solid transparent; border-left: 10px solid var(--white); }
  .headline, .cta { position: absolute; font-weight: 700; text-transform: uppercase; line-height: 1.05; white-space: nowrap; }
  .headline span { display: block; }
  .cta .call { font-weight: 400; display: block; }
  .cta .phone { color: var(--phone); font-weight: 400; display: block; }
  .brand { position: absolute; display: flex; align-items: center; gap: 10px; }
  .brand-mark { width: 34px; height: 34px; border: 3px solid var(--navy-mid); flex: none; }
  .brand-name { color: var(--brand-blue); font-weight: 700; line-height: 1; letter-spacing: .5px; white-space: nowrap; }

  /* Skyscraper */
  .ad-skyscraper { left: 65px; top: 68px; width: 187px; height: 699px; }
  .ad-skyscraper .panel-dark { left: 0; top: 0; width: 100%; height: 562px; }
  .ad-skyscraper .photo { left: 0; top: 330px; width: 100%; height: 232px; }
  .ad-skyscraper .band { left: 0; top: 562px; width: 100%; height: 9px; }
  .ad-skyscraper .notch-up { left: 38px; top: 552px; }
  .ad-skyscraper .headline { left: 0; top: 14px; width: 100%; text-align: center; }
  .ad-skyscraper .headline .l1 { font-size: 38px; }
  .ad-skyscraper .headline .l2 { font-size: 35px; margin-top: 4px; }
  .ad-skyscraper .headline .l3 { font-size: 31px; margin-top: 4px; }
  .ad-skyscraper .cta { left: 0; top: 182px; width: 100%; text-align: center; }
  .ad-skyscraper .cta .call { font-size: 28px; }
  .ad-skyscraper .cta .phone { font-size: 28px; margin-top: 2px; }
  .ad-skyscraper .brand { left: 14px; top: 616px; }
  .ad-skyscraper .brand-mark { width: 30px; height: 30px; }
  .ad-skyscraper .brand-name { font-size: 26px; }

  /* Large rectangle */
  .ad-rect-large { left: 275px; top: 169px; width: 393px; height: 327px; }
  .ad-rect-large .panel-dark { left: 0; top: 0; width: 100%; height: 204px; }
  .ad-rect-large .photo { left: 0; top: 0; width: 145px; height: 204px; }
  .ad-rect-large .band { left: 0; top: 204px; width: 100%; height: 9px; }
  .ad-rect-large .notch-up { left: 22px; top: 194px; }
  .ad-rect-large .headline { right: 18px; top: 20px; text-align: right; }
  .ad-rect-large .headline .l1 { font-size: 22px; }
  .ad-rect-large .headline .l2 { font-size: 41px; }
  .ad-rect-large .cta { left: 190px; width: 186px; top: 118px; text-align: center; }
  .ad-rect-large .cta .call { font-size: 28px; }
  .ad-rect-large .cta .phone { font-size: 27px; }
  .ad-rect-large .brand { left: 80px; top: 246px; }
  .ad-rect-large .brand-mark { width: 46px; height: 46px; }
  .ad-rect-large .brand-name { font-size: 40px; }

  /* Medium rectangle */
  .ad-rect-medium { left: 700px; top: 169px; width: 350px; height: 292px; }
  .ad-rect-medium .panel-dark { left: 0; top: 0; width: 100%; height: 181px; }
  .ad-rect-medium .photo { left: 0; top: 0; width: 125px; height: 181px; }
  .ad-rect-medium .band { left: 0; top: 181px; width: 100%; height: 8px; }
  .ad-rect-medium .notch-up { left: 20px; top: 172px; }
  .ad-rect-medium .headline { right: 14px; top: 18px; text-align: right; }
  .ad-rect-medium .headline .l1 { font-size: 20px; }
  .ad-rect-medium .headline .l2 { font-size: 37px; }
  .ad-rect-medium .cta { left: 160px; width: 182px; top: 104px; text-align: center; }
  .ad-rect-medium .cta .call { font-size: 26px; }
  .ad-rect-medium .cta .phone { font-size: 26px; }
  .ad-rect-medium .brand { left: 70px; top: 218px; }
  .ad-rect-medium .brand-mark { width: 42px; height: 42px; }
  .ad-rect-medium .brand-name { font-size: 34px; }

  /* Banner */
  .ad-banner { left: 275px; top: 531px; width: 545px; height: 68px; }
  .ad-banner .panel-dark { left: 139px; top: 0; width: 406px; height: 100%; }
  .ad-banner .notch-right { left: 139px; top: 18px; }
  .ad-banner .photo { left: 318px; top: 0; width: 74px; height: 100%; }
  .ad-banner .headline { left: 151px; top: 6px; }
  .ad-banner .headline .l1 { font-size: 16px; }
  .ad-banner .headline .l2 { font-size: 27px; }
  .ad-banner .cta { left: 402px; top: 10px; width: 136px; text-align: center; }
  .ad-banner .cta .call { font-size: 20px; }
  .ad-banner .cta .phone { font-size: 19px; }
  .ad-banner .brand { left: 8px; top: 21px; gap: 6px; }
  .ad-banner .brand-mark { width: 24px; height: 24px; border-width: 2px; }
  .ad-banner .brand-name { font-size: 22px; }

  /* Leaderboard */
  .ad-leaderboard { left: 275px; top: 622px; width: 848px; height: 103px; }
  .ad-leaderboard .panel-dark { left: 215px; top: 0; width: 633px; height: 100%; }
  .ad-leaderboard .notch-right { left: 215px; top: 16px; }
  .ad-leaderboard .photo { left: 492px; top: 0; width: 140px; height: 100%; }
  .ad-leaderboard .headline { left: 236px; top: 9px; }
  .ad-leaderboard .headline .l1 { font-size: 25px; }
  .ad-leaderboard .headline .l2 { font-size: 46px; }
  .ad-leaderboard .cta { left: 644px; top: 16px; width: 196px; text-align: center; }
  .ad-leaderboard .cta .call { font-size: 30px; }
  .ad-leaderboard .cta .phone { font-size: 29px; }
  .ad-leaderboard .brand { left: 14px; top: 32px; }
  .ad-leaderboard .brand-mark { width: 40px; height: 40px; }
  .ad-leaderboard .brand-name { font-size: 34px; }
</style>
</head>
<body>

<section class="ad ad-skyscraper" aria-label="Skyscraper ad">
  <div class="panel-dark"></div>
  <div class="photo" role="img" aria-label="Smiling customer support agent wearing a headset"></div>
  <div class="band"></div>
  <div class="notch-up"></div>
  <h2 class="headline"><span class="l1">Have Car</span><span class="l2">Transport</span><span class="l3">Questions?</span></h2>
  <p class="cta"><span class="call">Call Now</span><span class="phone">1-888-514-2763</span></p>
  <div class="brand"><span class="brand-mark"></span><span class="brand-name">ROVALEN</span></div>
</section>

<section class="ad ad-rect-large" aria-label="Large rectangle ad">
  <div class="panel-dark"></div>
  <div class="photo" role="img" aria-label="Smiling customer support agent wearing a headset"></div>
  <div class="band"></div>
  <div class="notch-up"></div>
  <h2 class="headline"><span class="l1">Have Car Transport</span><span class="l2">Questions?</span></h2>
  <p class="cta"><span class="call">Call Now</span><span class="phone">1-888-514-2763</span></p>
  <div class="brand"><span class="brand-mark"></span><span class="brand-name">ROVALEN</span></div>
</section>

<section class="ad ad-rect-medium" aria-label="Medium rectangle ad">
  <div class="panel-dark"></div>
  <div class="photo" role="img" aria-label="Smiling customer support agent wearing a headset"></div>
  <div class="band"></div>
  <div class="notch-up"></div>
  <h2 class="headline"><span class="l1">Have Car Transport</span><span class="l2">Questions?</span></h2>
  <p class="cta"><span class="call">Call Now</span><span class="phone">1-888-514-2763</span></p>
  <div class="brand"><span class="brand-mark"></span><span class="brand-name">ROVALEN</span></div>
</section>

<section class="ad ad-banner" aria-label="Banner ad">
  <div class="panel-dark"></div>
  <div class="notch-right"></div>
  <div class="photo" role="img" aria-label="Smiling customer support agent wearing a headset"></div>
  <h2 class="headline"><span class="l1">Have Car Transport</span><span class="l2">Questions?</span></h2>
  <p class="cta"><span class="call">Call Now</span><span class="phone">1-888-514-2763</span></p>
  <div class="brand"><span class="brand-mark"></span><span class="brand-name">ROVALEN</span></div>
</section>

<section class="ad ad-leaderboard" aria-label="Leaderboard ad">
  <div class="panel-dark"></div>
  <div class="notch-right"></div>
  <div class="photo" role="img" aria-label="Smiling customer support agent wearing a headset"></div>
  <h2 class="headline"><span class="l1">Have Car Transport</span><span class="l2">Questions?</span></h2>
  <p class="cta"><span class="call">Call Now</span><span class="phone">1-888-514-2763</span></p>
  <div class="brand"><span class="brand-mark"></span><span class="brand-name">ROVALEN</span></div>
</section>

</body>
</html>
```